Business Card Design Project

i have the logo designed.
I require designs for the managing director and the general manager.
we need space for email, and a mobile number.
any other cool stuff/design you guys just let me see what you got.
The managing director card could be black, minimalist, and the cards for the rest of the company could be using the green logo.
it has to impress. transportation market is fragmented, we want to appear professional and sophisticated.
Md: Tariq walid hussain
General manager: nabil hussain
Target Market(s)
clients: procurement heads of contracting companies
Industry/Entity Type
Business

```html
<!DOCTYPE html>
<html lang="en">
<head>
<meta charset="utf-8">
<title>Stridewell — Managing Director Business Card</title>
<link rel="stylesheet" href="https://fonts.googleapis.com/css2?family=Roboto:wght@300;400;500;700&display=swap">
<style>
  :root {
    --stage: #121212;
    --card-front: #0b0b0b;
    --card-back: #1d1d1d;
    --card-band: #262626;
    --ink: #f2f2f2;
    --ink-muted: #9a9a9a;
    --ink-faint: #6d6d6d;
  }
  * { box-sizing: border-box; margin: 0; padding: 0; }
  html, body {
    width: 1200px; height: 900px; overflow: hidden;
    background: var(--stage);
    font-family: "Roboto", sans-serif;
  }
  .canvas { position: relative; width: 1200px; height: 900px; }

  .card {
    position: absolute;
    width: 640px; height: 366px;
    left: 280px;
    border-radius: 2px;
    overflow: hidden;
  }

  /* Front */
  .card--front { top: 64px; background: var(--card-front); }
  .brand {
    position: absolute; left: 0; right: 0; top: 130px;
    display: flex; align-items: center; justify-content: center; gap: 18px;
  }
  .brand__dot {
    width: 22px; height: 22px; border-radius: 50%;
    background: var(--ink);
  }
  .brand__name {
    font-size: 56px; font-weight: 700; color: var(--ink);
    letter-spacing: 1px;
  }
  .website {
    position: absolute; left: 0; right: 0; top: 232px;
    text-align: center;
    font-size: 15px; font-weight: 300; color: var(--ink-faint);
    letter-spacing: 9px;
  }

  /* Back */
  .card--back { top: 470px; background: var(--card-back); }
  .band {
    position: absolute; left: 0; right: 0; height: 44px;
    background: var(--card-band);
  }
  .band--top { top: 0; }
  .band--bottom { bottom: 0; }

  .identity {
    position: absolute; left: 0; top: 192px;
    padding-left: 30px;
    border-left: 6px solid var(--ink);
  }
  .identity__name {
    font-size: 21px; font-weight: 700; color: var(--ink);
    letter-spacing: 1px; text-transform: uppercase;
  }
  .identity__title {
    margin-top: 6px;
    font-size: 19px; font-weight: 300; color: var(--ink-muted);
    letter-spacing: 0.5px;
  }

  .contact {
    position: absolute; left: 368px; top: 92px;
    display: grid; gap: 12px;
  }
  .contact__row { display: flex; align-items: flex-start; gap: 14px; }
  .contact__icon { width: 20px; height: 20px; flex: none; margin-top: 1px; }
  .contact__text {
    font-size: 15px; font-weight: 300; color: var(--ink-muted);
    letter-spacing: 1px; line-height: 1.25;
  }
</style>
</head>
<body>
<main class="canvas">

  <section class="card card--front" aria-label="Card front">
    <div class="brand">
      <span class="brand__dot"></span>
      <span class="brand__name">Stridewell</span>
    </div>
    <p class="website">stridewell.au</p>
  </section>

  <section class="card card--back" aria-label="Card back">
    <div class="band band--top"></div>
    <div class="band band--bottom"></div>

    <div class="identity">
      <p class="identity__name">Tariq Walid Hussain</p>
      <p class="identity__title">Managing Director</p>
    </div>

    <div class="contact">
      <div class="contact__row">
        <svg class="contact__icon" viewBox="0 0 20 20" aria-hidden="true">
          <rect x="2" y="5" width="16" height="11" fill="var(--ink)"/>
          <polyline points="2,5 10,11.5 18,5" fill="none" stroke="var(--card-back)" stroke-width="1.4"/>
        </svg>
        <span class="contact__text">tariq@stridewell.com</span>
      </div>
      <div class="contact__row">
        <svg class="contact__icon" viewBox="0 0 20 20" aria-hidden="true">
          <rect x="5" y="1.5" width="10" height="17" rx="1.8" fill="none" stroke="var(--ink)" stroke-width="1.5"/>
          <line x1="8.5" y1="15.5" x2="11.5" y2="15.5" stroke="var(--ink)" stroke-width="1.3"/>
        </svg>
        <span class="contact__text">+484 2210 9087<br>+484 0561 3398</span>
      </div>
    </div>
  </section>

</main>
</body>
</html>
```